Hero Image for Homepage Header

I need an hero image (main image) for a new web site.
The site will be a sales consultancy/coaching business aimed at B2B software sales professionals and software/SaaS firms. The aim of the business is to help sales professionals and tech firms transform their sales performance and close more deals.

The two styles of hero images I like can be seen here:
- Vantorify.com
- Pluvetic.com

You can come up with a concept that is like one of these.

Basically the image should show a familiar UI screen of a sales professional's CRM dashboard (see attachments).
In the animated gif (which I hate - it's poor quality) you can see how the data points all improve. This represents the sales 'transformation'.

I'd like you to re-create a UI screen from gravindel.com (the attachments, Gravindel1 and Gravindel2 are taken from the Gravindel CRM software. I want you to recreate them from scratch but in a more high-quality manner and come up with a hero image design concept that will show how poor results on screen can become better.
The attachment Gravindel2 shows how the results from Gravindel1 have been improved.

If you think an animated gif would be better, that's fine.

I'd like your design concept to include the following points (in freehand text style just like in the Vantorify.com image)

- 4x pipeline
- Higher conversions
- More deals CLOSED-WON

Come up with something stunning

```html
<!DOCTYPE html>
<html lang="en">
<head>
<meta charset="utf-8">
<title>Transform your sales performance</title>
<link rel="stylesheet" href="https://fonts.googleapis.com/css2?family=Permanent+Marker&family=Roboto:wght@400;500;700;900&display=swap">
<style>
  :root {
    --ink: #0d0d0d;
    --button: #1ca0dc;
    --blob: #eef0f9;
    --panel: #f7f8fb;
    --panel-line: #e4e7ee;
    --card: #ffffff;
    --teal: #0e6b63;
    --red: #f50f0f;
    --orange: #f2a93b;
    --sparkle-blue: #1e9be0;
    --gauge-red: #e0161f;
    --gauge-blue: #1f3fe0;
    --gauge-green: #8cc63f;
    --dash-red: #c8202a;
    --dash-navy: #2b3a8c;
    --dash-green: #1a7a3a;
    --needle: #1e2a44;
    --link: #2a7bd1;
    --muted: #4a4f5a;
  }
  * { box-sizing: border-box; margin: 0; padding: 0; }
  html, body { width: 1200px; height: 515px; overflow: hidden; background: #fff; }
  body { position: relative; font-family: "Roboto", sans-serif; color: var(--ink); }

  .hero-copy { position: absolute; left: 68px; top: 96px; width: 460px; }
  .hero-title { font-weight: 700; font-size: 44px; line-height: 49px; letter-spacing: -0.3px; margin-left: 3px; }
  .hero-text { margin-top: 42px; width: 450px; font-size: 11px; line-height: 14px; font-weight: 500; }
  .hero-actions { position: absolute; left: 71px; top: 346px; display: flex; gap: 23px; }
  .hero-button { width: 167px; height: 42px; background: var(--button); border-radius: 2px; border: none; }

  .stage { position: absolute; inset: 0; pointer-events: none; }
  .note { position: absolute; z-index: 5; font-family: "Permanent Marker", "Roboto", sans-serif; font-size: 20px; line-height: 24px; color: var(--ink); letter-spacing: 0.3px; white-space: nowrap; }
  .note--pipeline { left: 598px; top: 36px; }
  .note--conversions { left: 1066px; top: 76px; transform: rotate(33deg); transform-origin: left top; font-size: 18px; line-height: 19px; }
  .note--deals { left: 578px; top: 340px; font-size: 18px; line-height: 24px; }

  .dashboard { position: absolute; left: 594px; top: 70px; width: 431px; height: 204px; background: var(--panel); box-shadow: 0 4px 14px rgba(40,50,90,.12); overflow: hidden; }
  .dashboard-bar { height: 14px; background: #fff; display: flex; align-items: center; padding: 0 4px; gap: 3px; border-bottom: 1px solid var(--panel-line); }
  .dashboard-bar .mark { width: 7px; height: 7px; background: var(--red); }
  .dashboard-bar .title { font-size: 3.6px; line-height: 4px; font-weight: 500; }
  .dashboard-bar .tools { margin-left: auto; font-size: 3.4px; color: var(--link); display: flex; gap: 10px; }
  .dashboard-grid { display: grid; grid-template-columns: 135px 176px 120px; grid-template-rows: 88px 88px; gap: 1px; background: var(--panel-line); padding-top: 8px; background-clip: content-box; }
  .tile { background: var(--panel); position: relative; padding: 4px 5px; font-size: 3.6px; line-height: 4.2px; color: var(--muted); overflow: hidden; }
  .tile h4 { font-size: 3.8px; font-weight: 500; color: var(--ink); }
  .tile .gauge { position: absolute; left: 19px; top: 14px; }
  .tile .value { position: absolute; left: 52px; top: 66px; }
  .tile .foot { position: absolute; left: 5px; bottom: 6px; }
  .tile .foot a { color: var(--link); text-decoration: none; display: block; }
  .tile .big { position: absolute; left: 20px; top: 24px; font-size: 24px; line-height: 24px; color: var(--teal); font-weight: 500; white-space: nowrap; }
  .funnel { position: absolute; left: 66px; top: 16px; width: 36px; font-size: 3.4px; text-align: center; color: #fff; font-weight: 700; }
  .funnel .cap { color: var(--muted); font-weight: 500; margin-bottom: 1px; }
  .funnel span { display: block; height: 8.5px; line-height: 8.5px; margin: 0 auto; }
  .legend { position: absolute; right: 10px; top: 24px; font-size: 2.6px; line-height: 6.5px; text-align: right; }
  .legend i { display: inline-block; width: 3px; height: 3px; margin-left: 2px; vertical-align: middle; }
  .table-mini { position: absolute; left: 5px; top: 24px; width: 44px; border: 0.5px solid var(--link); font-size: 2.2px; line-height: 3.2px; color: var(--link); }
  .table-mini div { border-bottom: 0.4px solid #c9d6ec; padding-left: 1px; }

  .mrr-card { position: absolute; left: 705px; top: 302px; width: 222px; height: 119px; background: var(--card); border-radius: 4px; box-shadow: 0 6px 20px rgba(40,50,90,.14); overflow: hidden; }
  .mrr-card h3 { position: absolute; left: 13px; top: 10px; font-size: 5.4px; line-height: 6px; font-weight: 500; }
  .mrr-card h3 small { display: block; font-weight: 400; color: var(--muted); font-size: 4.2px; }
  .mrr-card .foot { position: absolute; left: 13px; top: 97px; font-size: 4.4px; line-height: 6px; color: var(--muted); }
  .mrr-card .foot a { color: var(--link); font-size: 3.2px; text-decoration: none; display: block; line-height: 4px; }
  .mrr-card svg { position: absolute; left: 0; top: 0; }

  .acv-card { position: absolute; left: 949px; top: 144px; width: 121px; height: 253px; background: var(--card); border-radius: 6px; box-shadow: 0 8px 24px rgba(40,50,90,.16); padding: 19px 12px; }
  .acv-card h2 { font-size: 21px; line-height: 27px; font-weight: 500; }
  .acv-card p { margin-top: 7px; font-size: 9px; line-height: 11px; font-weight: 500; }
  .acv-card .before { position: absolute; left: 16px; top: 200px; font-size: 33px; line-height: 34px; color: var(--teal); font-weight: 500; white-space: nowrap; }
  .acv-badge { position: absolute; left: 1009px; top: 277px; width: 132px; height: 56px; background: var(--red); border-radius: 5px; color: #fff; font-size: 37px; font-weight: 500; display: flex; align-items: center; justify-content: center; white-space: nowrap; box-shadow: 0 6px 14px rgba(245,15,15,.25); }
</style>
</head>
<body>

<section class="hero-copy">
  <h1 class="hero-title">Transform your sales performance and close more deals</h1>
  <p class="hero-text">Lorem ipsum dolor sit amet, consectetuer adipiscing elit, sed diam nonummy nibh euismod tincidunt ut laoreet dolore magna aliquam erat volutpat. Ut wisi enim ad minim veniam, quis nostrud exerci tation ullamcorper suscipit lobortis nisl ut aliquip ex ea com</p>
</section>
<div class="hero-actions">
  <button class="hero-button" aria-label="Primary action"></button>
  <button class="hero-button" aria-label="Secondary action"></button>
</div>

<svg class="stage" width="1200" height="515" viewBox="0 0 1200 515" aria-hidden="true">
  <defs>
    <symbol id="sparkle" viewBox="0 0 20 20">
      <path d="M10 0 C11 8 12 9 20 10 C12 11 11 12 10 20 C9 12 8 11 0 10 C8 9 9 8 10 0Z"/>
    </symbol>
  </defs>
  <path d="M820 40 C880 30 930 60 960 52 C1010 40 1060 70 1050 120 C1045 160 1075 200 1090 250 C1100 300 1075 350 1050 380 C1020 420 960 450 900 445 C850 440 820 460 780 440 C740 420 700 420 690 380 C680 320 700 280 710 240 C720 180 740 80 820 40Z" fill="var(--blob)"/>
  <path d="M720 48 C760 56 790 72 810 98" fill="none" stroke="var(--orange)" stroke-width="2" stroke-linecap="round"/>
  <path d="M802 94 L810 99 L811 89" fill="none" stroke="var(--orange)" stroke-width="2" stroke-linecap="round" stroke-linejoin="round"/>
  <path d="M1113 184 C1118 210 1108 228 1090 240" fill="none" stroke="var(--orange)" stroke-width="2" stroke-linecap="round"/>
  <path d="M1088 231 L1088 241 L1097 240" fill="none" stroke="var(--orange)" stroke-width="2" stroke-linecap="round" stroke-linejoin="round"/>
  <path d="M683 352 C700 342 715 340 727 348" fill="none" stroke="var(--orange)" stroke-width="2" stroke-linecap="round"/>
  <path d="M721 343 L728 349 L721 353" fill="none" stroke="var(--orange)" stroke-width="2" stroke-linecap="round" stroke-linejoin="round"/>
  <path d="M972 333 C977 318 990 306 1005 303" fill="none" stroke="var(--orange)" stroke-width="2" stroke-linecap="round"/>
  <path d="M998 299 L1006 303 L1000 310" fill="none" stroke="var(--orange)" stroke-width="2" stroke-linecap="round" stroke-linejoin="round"/>
  <use href="#sparkle" x="580" y="264" width="22" height="22" fill="var(--orange)"/>
  <use href="#sparkle" x="963" y="427" width="48" height="48" fill="var(--sparkle-blue)"/>
</svg>

<div class="dashboard">
  <div class="dashboard-bar"><span class="mark"></span><span class="title">Dashboard<br>Sales Rep Dashboard</span><span class="tools"><span>Refresh</span><span>Edit</span><span>▾</span></span></div>
  <div class="dashboard-grid">
    <div class="tile">
      <h4>MTD Total MRR</h4>MTD Closed Won Opportunities
      <svg class="gauge" width="90" height="52" viewBox="0 0 90 52">
        <path d="M5.2 49.5 A40 40 0 0 1 19.3 15.4" fill="none" stroke="var(--dash-red)" stroke-width="2.4"/>
        <path d="M19.3 15.4 A40 40 0 0 1 61.9 9.7" fill="none" stroke="var(--dash-navy)" stroke-width="2.4"/>
        <path d="M61.9 9.7 A40 40 0 0 1 84.8 49.5" fill="none" stroke="var(--dash-green)" stroke-width="2.4"/>
        <line x1="45" y1="46" x2="19" y2="34" stroke="var(--needle)" stroke-width="2.4" stroke-linecap="round"/>
      </svg>
      <div class="value">$ 21K (16%)</div>
      <div class="foot">Drill into report to see details<a>View Report (SR: Closed Won Opportunities MRR)</a></div>
    </div>
    <div class="tile">
      <h4>MTD Your Pipeline Opportunities</h4>MTD Your Pipeline Opportunities
      <div class="funnel"><div class="cap">Sum of Amount</div>
        <span style="width:34px;background:#22a3e0">$7K</span><span style="width:30px;background:#16375e">$11K</span><span style="width:27px;background:#7fd1d1">$9K</span><span style="width:24px;background:#22b3a0">$29K</span><span style="width:21px;background:#e9c46a">$21K</span><span style="width:18px;background:#f5a623">$9K</span></div>
      <div class="legend">Stage<br>Initial Contact<i style="background:#22a3e0"></i><br>Discovery Call<i style="background:#16375e"></i><br>Demo Delivered<i style="background:#7fd1d1"></i><br>Technical Validation<i style="background:#22b3a0"></i><br>Proposal<i style="background:#e9c46a"></i><br>Negotiation<i style="background:#f5a623"></i></div>
      <div class="foot">Drill into report to see details<a>View Report (SR: Closed Won Opportunities MTD)</a></div>
    </div>
    <div class="tile">
      <h4>FYTD Total ACV</h4>FYTD Closed Won Opportunities
      <div class="big">$1.1 M</div>
      <div class="foot">Drill into report to see details<a>View Report (SR: Closed Won)</a></div>
    </div>
    <div class="tile">
      <h4>FYTD Total ARR</h4>FYTD Closed Won Opportunities
      <svg class="gauge" width="90" height="52" viewBox="0 0 90 52">
        <path d="M5.2 49.5 A40 40 0 0 1 19.3 15.4" fill="none" stroke="var(--dash-red)" stroke-width="2.4"/>
        <path d="M19.3 15.4 A40 40 0 0 1 61.9 9.7" fill="none" stroke="var(--dash-navy)" stroke-width="2.4"/>
        <path d="M61.9 9.7 A40 40 0 0 1 84.8 49.5" fill="none" stroke="var(--dash-green)" stroke-width="2.4"/>
        <line x1="45" y1="46" x2="43" y2="17" stroke="var(--needle)" stroke-width="2.4" stroke-linecap="round"/>
      </svg>
      <div class="value">$ 726 (47%)</div>
      <div class="foot">Drill into report to see details<a>View Report (SR: Closed Won Opportunities ARR)</a></div>
    </div>
    <div class="tile">
      <h4>MTD Your Pipeline Opportunities</h4>MTD Your Pipeline Opportunities
      <div class="funnel"><div class="cap">Sum of Amount</div>
        <span style="width:34px;background:#22a3e0">$109K</span><span style="width:30px;background:#16375e">$118K</span><span style="width:27px;background:#7fd1d1">$328K</span><span style="width:24px;background:#22b3a0">$255K</span><span style="width:21px;background:#e9c46a">$204K</span><span style="width:18px;background:#f5a623">$88K</span></div>
      <div class="legend">Stage<br>Initial Contact<i style="background:#22a3e0"></i><br>Discovery Call<i style="background:#16375e"></i><br>Demo Delivered<i style="background:#7fd1d1"></i><br>Technical Validation<i style="background:#22b3a0"></i><br>Proposal<i style="background:#e9c46a"></i><br>Negotiation<i style="background:#f5a623"></i></div>
      <div class="foot">Drill into report to see details<a>View Report (SR: Closed Won Opportunities MTD)</a></div>
    </div>
    <div class="tile">
      <h4>Your 10 Opportunities</h4>FYTD Top 10 Opportunities
      <div class="table-mini"><div>Opportunity Name</div><div>Northline</div><div>Orbis</div><div>Credit Valley</div><div>Kestrel</div><div>Haldor</div><div>Small Ops</div><div>Brightpath</div><div>New York Prospect</div><div>Lakeview</div><div>Meridian</div></div>
      <div class="foot">Drill into report to see details<a>View Report (SR: Closed Won)</a></div>
    </div>
  </div>
</div>

<div class="mrr-card">
  <h3>MTD Total MRR<small>MTD Closed Won Opportunities</small></h3>
  <svg width="222" height="119" viewBox="0 0 222 119">
    <path d="M52.3 85.9 A68 68 0 0 1 76.3 27.9" fill="none" stroke="var(--gauge-red)" stroke-width="4"/>
    <path d="M76.3 27.9 A68 68 0 0 1 148.7 18.4" fill="none" stroke="var(--gauge-blue)" stroke-width="4"/>
    <path d="M148.7 18.4 A68 68 0 0 1 187.7 85.9" fill="none" stroke="var(--gauge-green)" stroke-width="4"/>
    <g font-family="Roboto, sans-serif" font-size="3.8" fill="#333" text-anchor="middle">
      <text x="68" y="86">$0</text><text x="69" y="73">$10K</text><text x="73" y="62">$20K</text><text x="80" y="50">$30K</text><text x="89" y="41">$40K</text><text x="101" y="35">$50K</text><text x="113" y="31">$60K</text><text x="127" y="31">$70K</text><text x="139" y="35">$80K</text><text x="151" y="41">$90K</text><text x="160" y="50">$100K</text><text x="166" y="62">$110K</text><text x="170" y="73">$120K</text><text x="170" y="86">$130K</text>
    </g>
    <path d="M118 78 L174 81 L174 85 L118 84 Z" fill="var(--needle)"/>
    <circle cx="118" cy="81" r="3" fill="var(--needle)"/>
    <text x="122" y="104" font-family="Roboto, sans-serif" font-size="6" fill="#333" text-anchor="middle">$194K</text>
  </svg>
  <div class="foot">Drill into report to see details<a>View Report (SR: Closed Won Opportunities MRR)</a></div>
</div>

<div class="acv-card">
  <h2>FYTD<br>Total ACV</h2>
  <p>FYTD Closed<br>Won Opportunities</p>
  <div class="before">$1.1 M</div>
</div>
<div class="acv-badge">$4.2 M</div>

<div class="note note--pipeline">4X PIPELINE</div>
<div class="note note--conversions">HIGHER<br>CONVERSIONS</div>
<div class="note note--deals">MORE DEALS<br>CLOSED-WON</div>

</body>
</html>
```